Professional / Luxury Rack Card Design Needed (Do not use AI)

We are a private, boutique style optometry practice in College Station, Texas. We want the new design to communicate a premium, modern, luxury eye care experience while remaining professional and approachable.
When someone picks up this rack card, we want them to think:
"This practice looks modern, advanced, trustworthy, and premium. I would expect exceptional care and a high-end eyewear experience."

Target Market(s)

Families, professionals, adults seeking comprehensive medical eye care and vision correction. Patients seeking premium eyewear, advanced technology, and personalize care. Individuals and families seeking long term relationships with a trusted eye care provider. Patients who value exceptional service, expertise, and convenience.

Industry/Entity Type

Medical & Optometry-luxury optical

Font styles to use
Serif
Other font styles liked:
• Avenir if available. If not, Montserrat for headlines and Open Sans for Body text. For the slogan, use larger bold Montserrat.

Requirements
Must have
• Non-edited photo of doctors (merged together) with names. "Your Vision. Our Focus." Phone, website, Text/Call to Schedule appointment (Call to action to schedule). Accepting new patients. Eye Care center logo prominently displayed. Real photo of Eye Care Center building. Contact information (see attachement with all info)
Nice to have
• For frame brands, use the branded names. (see attachment)
Should not have
• Shouild not be busy/cluttered. Do not use scripted font from my website. Do NOT use AI generated images. Do not edit doctor faces other than merging them together. DO NOT use AI to edit faces....only to merge them side by side.

```html
<!DOCTYPE html>
<html lang="en">
<head>
<meta charset="utf-8">
<title>Clearview Eye Studio – Rack Card</title>
<link href="https://fonts.googleapis.com/css2?family=Jost:wght@400;500;600;700&display=swap" rel="stylesheet">
<style>
:root{
  --stage:#9b9b9b;
  --card:#ffffff;
  --ink:#232323;
  --ink-soft:#3a3a3a;
  --gold:#cdb92e;
  --sky:#a9d1e4;
  --sky-pale:#e6f1f7;
  --ring:#5e5e5e;
  --mist:#efefef;
  --navy:#1f3a5c;
}
*{margin:0;padding:0;box-sizing:border-box}
html,body{width:1144px;height:1200px;overflow:hidden}
body{background:var(--stage);position:relative;font-family:"Jost",sans-serif;color:var(--ink)}
.card{position:absolute;top:97px;width:447px;height:1007px;background:var(--card);overflow:hidden;box-shadow:0 6px 24px rgba(0,0,0,.25)}
.card--front{left:108px}
.card--back{left:590px}
.abs{position:absolute}

/* front */
.hero-ring{left:0;top:6px;width:530px;height:478px}
.hero-photo{left:100px;top:48px;width:395px;height:395px;border-radius:50%;
  background:linear-gradient(180deg,#e4ebf4 0%,#dfe4ea 35%,#d9c7a0 55%,#a98c64 75%,#6f8a4b 92%,#b9b2a6 100%)}
.brand{left:166px;top:114px;display:flex;align-items:center;gap:10px}
.brand__dot{width:30px;height:30px;border-radius:50%;background:var(--ring)}
.brand__name{font-size:22px;font-weight:500;color:var(--ring);line-height:1}
.brand__member{display:block;font-size:8px;letter-spacing:1.5px;text-transform:uppercase;margin-top:5px;font-weight:500}
.slogan{left:0;width:447px;text-align:center;font-weight:600;font-size:50px;line-height:1;letter-spacing:-.5px}
.slogan--1{top:490px;padding-left:10px}
.slogan--2{top:546px;color:var(--gold)}
.perks{left:56px;top:606px;list-style:none}
.perk{display:flex;align-items:center;height:70px;font-size:21px;color:var(--ink-soft);letter-spacing:.3px;line-height:1.3}
.perk svg{width:62px;height:52px;margin-right:18px;flex:none}
.cta{left:18px;top:896px;width:411px;height:41px;background:var(--gold);border-radius:4px;color:#fff;font-weight:500;font-size:18px;letter-spacing:.6px;display:flex;align-items:center;justify-content:center}
.new-patients{left:0;top:948px;width:447px;text-align:center;font-weight:600;font-size:22px;letter-spacing:.3px}
.wave-bottom{left:0;bottom:0;width:447px;height:20px}

/* back */
.wave-top{left:0;top:0;width:447px;height:18px}
.services-bg{left:0;top:366px;width:447px;height:378px;background:linear-gradient(180deg,#fff 0%,var(--sky-pale) 25%,var(--sky-pale) 100%)}
.section-title{left:0;width:447px;text-align:center;font-size:28px;font-weight:500}
.section-title em{font-style:normal;color:var(--gold)}
.rule{left:176px;width:95px;height:2px;background:var(--sky)}
.doctor{width:170px;text-align:center}
.doctor__photo{width:104px;height:104px;border-radius:50%;margin:0 auto 14px;background:radial-gradient(circle at 50% 60%,#f1f1f1 0%,#d2c6b4 45%,#8f7a60 100%)}
.doctor__name{font-size:14px;white-space:nowrap}
.service{display:flex;align-items:center;width:210px;font-size:12.5px;line-height:1.45;color:var(--ink-soft)}
.service svg{width:54px;height:44px;margin-right:12px;flex:none}
.frames-band{left:0;top:744px;width:447px;height:160px;background:var(--mist)}
.frames-title{left:0;top:762px;width:447px;text-align:center;font-size:17px;font-weight:500}
.frames-title em{font-style:normal;color:var(--gold)}
.label-row{left:30px;width:390px;display:flex;justify-content:space-between;font-size:9.5px;font-weight:600;letter-spacing:.6px;color:#333;text-transform:uppercase}
.more{left:308px;top:861px;font-size:6.5px;letter-spacing:1px;color:#4a7d99;font-weight:600}
.contact-band{left:0;top:870px;width:447px;height:137px}
.contact{display:flex;align-items:center;font-size:11.5px;line-height:1.45;color:var(--ink)}
.contact__icon{width:33px;height:33px;border-radius:50%;background:#fff;display:flex;align-items:center;justify-content:center;margin-right:14px;flex:none}
</style>
</head>
<body>
<svg width="0" height="0" style="position:absolute">
  <defs>
    <symbol id="perk-frame" viewBox="0 0 62 52">
      <path d="M34 2 A24 24 0 1 0 34 50" fill="none" stroke="var(--ring)" stroke-width="3.5"/>
      <path d="M34 2 A24 24 0 0 1 56 22" fill="none" stroke="var(--ring)" stroke-width="2"/>
      <path d="M34 50 A24 24 0 0 0 56 30" fill="none" stroke="var(--ring)" stroke-width="2"/>
      <circle cx="31" cy="26" r="19" fill="var(--sky)"/>
    </symbol>
    <symbol id="svc-frame" viewBox="0 0 54 44">
      <path d="M27 2 A20 20 0 1 0 27 42" fill="none" stroke="#4b4b4b" stroke-width="3"/>
      <path d="M27 2 A20 20 0 0 1 47 18" fill="none" stroke="#4b4b4b" stroke-width="1.6"/>
      <path d="M27 42 A20 20 0 0 0 47 26" fill="none" stroke="#4b4b4b" stroke-width="1.6"/>
      <circle cx="26" cy="22" r="16" fill="#fff" stroke="#ddd" stroke-width=".8"/>
    </symbol>
  </defs>
</svg>

<!-- Front -->
<section class="card card--front">
  <svg class="abs hero-ring" viewBox="0 0 530 478">
    <path d="M470 30 C380 -10 250 5 150 60 C60 110 10 190 0 240 C20 330 110 440 250 470 C360 495 450 460 500 430 L500 405 C440 440 360 460 290 450 C170 430 90 340 90 240 C90 130 180 40 300 30 C380 22 440 40 500 70 L500 45Z" fill="var(--ring)"/>
  </svg>
  <div class="abs hero-photo" role="img" aria-label="Photo of the Clearview Eye Studio building with stone arches and tiled roof"></div>
  <div class="abs brand">
    <span class="brand__dot"></span>
    <span class="brand__name">Clearview Eye Studio<span class="brand__member">A member of Optica Network</span></span>
  </div>
  <h1 class="abs slogan slogan--1">Your Vision.</h1>
  <h2 class="abs slogan slogan--2">Our Focus</h2>
  <ul class="abs perks">
    <li class="perk"><svg viewBox="0 0 62 52"><use href="#perk-frame"/><path d="M21 26 Q31 17 41 26 Q31 35 21 26Z" fill="none" stroke="var(--ring)" stroke-width="1.6"/><circle cx="31" cy="26" r="3.5" fill="none" stroke="var(--ring)" stroke-width="1.6"/></svg>Comprehensive Eye Care</li>
    <li class="perk"><svg viewBox="0 0 62 52"><use href="#perk-frame"/><g fill="var(--ring)"><rect x="28" y="17" width="6" height="5"/><rect x="22" y="30" width="5" height="5"/><rect x="28.5" y="30" width="5" height="5"/><rect x="35" y="30" width="5" height="5"/></g><path d="M31 22v8M24.5 30v-3h13v3" fill="none" stroke="var(--ring)" stroke-width="1.4"/></svg>Advanced Technology</li>
    <li class="perk"><svg viewBox="0 0 62 52"><use href="#perk-frame"/><path d="M31 34 L22 25 A5 5 0 0 1 31 19 A5 5 0 0 1 40 25Z" fill="var(--ring)"/></svg>Personalized Care</li>
    <li class="perk"><svg viewBox="0 0 62 52"><use href="#perk-frame"/><circle cx="31" cy="26" r="7" fill="none" stroke="var(--ring)" stroke-width="3" stroke-dasharray="3 2"/><circle cx="31" cy="26" r="3" fill="var(--ring)"/></svg>Over 1,000 Designer<br>Frames &amp; Sunglasses</li>
  </ul>
  <div class="abs cta">SCHEDULE YOUR APPOINTMENT TODAY</div>
  <p class="abs new-patients">ACCEPTING NEW PATIENTS</p>
  <svg class="abs wave-bottom" viewBox="0 0 447 20" preserveAspectRatio="none"><path d="M0 20 V8 Q220 -4 370 20Z" fill="var(--sky)"/></svg>
</section>

<!-- Back -->
<section class="card card--back">
  <svg class="abs wave-top" viewBox="0 0 447 18" preserveAspectRatio="none"><path d="M0 0 H447 Q300 18 150 12 Q60 8 0 0Z" fill="var(--sky)"/></svg>
  <div class="abs services-bg"></div>

  <h2 class="abs section-title" style="top:22px">Meet Our <em>Doctors</em></h2>
  <div class="abs rule" style="top:64px"></div>

  <div class="abs doctor" style="left:51px;top:77px"><div class="doctor__photo" role="img" aria-label="Portrait photo of Dr. Helen Marsh"></div><p class="doctor__name">Dr. Helen Marsh, O.D.</p></div>
  <div class="abs doctor" style="left:225px;top:77px"><div class="doctor__photo" role="img" aria-label="Portrait photo of Dr. Claire Whitman"></div><p class="doctor__name">Dr. Claire Whitman, O.D.</p></div>
  <div class="abs doctor" style="left:51px;top:226px"><div class="doctor__photo" role="img" aria-label="Portrait photo of Dr. Paul Adler"></div><p class="doctor__name">Dr. Paul Adler, O.D.</p></div>
  <div class="abs doctor" style="left:225px;top:226px"><div class="doctor__photo" role="img" aria-label="Portrait photo of Dr. Nora Selim"></div><p class="doctor__name">Dr. Nora Selim, O.D.</p></div>

  <h2 class="abs section-title" style="top:400px">Our <em>Services</em></h2>
  <div class="abs rule" style="top:440px"></div>

  <div class="abs service" style="left:27px;top:461px"><svg viewBox="0 0 54 44"><use href="#svc-frame"/><path d="M17 22 Q26 14 35 22 Q26 30 17 22Z" fill="none" stroke="var(--gold)" stroke-width="1.2"/><circle cx="26" cy="22" r="3" fill="none" stroke="var(--gold)" stroke-width="1.2"/></svg>Comprehensive<br>Eye Exams</div>
  <div class="abs service" style="left:234px;top:461px"><svg viewBox="0 0 54 44"><use href="#svc-frame"/><ellipse cx="23" cy="22" rx="4" ry="7" fill="none" stroke="var(--gold)" stroke-width="1.2" transform="rotate(25 23 22)"/><ellipse cx="29" cy="23" rx="4" ry="7" fill="none" stroke="var(--gold)" stroke-width="1.2" transform="rotate(25 29 23)"/></svg>Speciality Contact<br>Lens Service</div>

  <div class="abs service" style="left:27px;top:514px"><svg viewBox="0 0 54 44"><use href="#svc-frame"/><circle cx="26" cy="18" r="4" fill="none" stroke="var(--gold)" stroke-width="1.2"/><path d="M18 30 Q26 21 34 30Z" fill="none" stroke="var(--gold)" stroke-width="1.2"/></svg>Pediatric Exams</div>
  <div class="abs service" style="left:234px;top:514px"><svg viewBox="0 0 54 44"><use href="#svc-frame"/><path d="M17 24 Q26 16 35 24 Q26 32 17 24Z" fill="none" stroke="var(--gold)" stroke-width="1.2"/><circle cx="26" cy="24" r="2.5" fill="none" stroke="var(--gold)" stroke-width="1.2"/><path d="M26 12v5M23 15h6" stroke="var(--gold)" stroke-width="1.2"/></svg>Surgery<br>Co-Management</div>

  <div class="abs service" style="left:27px;top:567px"><svg viewBox="0 0 54 44"><use href="#svc-frame"/><path d="M17 22 Q26 14 35 22 Q26 30 17 22Z" fill="none" stroke="var(--gold)" stroke-width="1.2"/><circle cx="26" cy="22" r="3" fill="none" stroke="var(--gold)" stroke-width="1.2"/></svg>Cataract, Glaucoma<br>Macular Degeneration</div>
  <div class="abs service" style="left:234px;top:567px"><svg viewBox="0 0 54 44"><use href="#svc-frame"/><path d="M26 13 Q33 22 33 25 A7 7 0 0 1 19 25 Q19 22 26 13Z" fill="none" stroke="var(--gold)" stroke-width="1.2"/></svg>Dry Eye &amp; Allergy</div>

  <div class="abs service" style="left:27px;top:620px"><svg viewBox="0 0 54 44"><use href="#svc-frame"/><path d="M22 32 V27 Q18 24 19 19 A7 7 0 0 1 33 19 Q33 22 34 24 L32 25 V29 H28 V32" fill="none" stroke="var(--gold)" stroke-width="1.2"/></svg>Migraine &amp; Headache</div>
  <div class="abs service" style="left:234px;top:620px"><svg viewBox="0 0 54 44"><use href="#svc-frame"/><path d="M17 22 Q26 14 35 22 Q26 30 17 22Z" fill="none" stroke="var(--gold)" stroke-width="1.2"/><circle cx="26" cy="22" r="3" fill="none" stroke="var(--gold)" stroke-width="1.2"/></svg>Eye Muscle Alignment</div>

  <div class="abs service" style="left:27px;top:673px"><svg viewBox="0 0 54 44"><use href="#svc-frame"/><path d="M26 13 L33 16 V22 Q33 28 26 31 Q19 28 19 22 V16Z" fill="none" stroke="var(--gold)" stroke-width="1.2"/><path d="M26 18v8M22 22h8" stroke="var(--gold)" stroke-width="1.2"/></svg>Eye Injuries &amp;<br>Infections</div>
  <div class="abs service" style="left:234px;top:673px"><svg viewBox="0 0 54 44"><use href="#svc-frame"/><path d="M18 17 H24 L26 19 H34 V30 H18Z" fill="none" stroke="var(--gold)" stroke-width="1.2"/><circle cx="26" cy="24.5" r="2" fill="none" stroke="var(--gold)" stroke-width="1.2"/></svg>Ocular Disease<br>Management</div>

  <div class="abs frames-band"></div>
  <h3 class="abs frames-title">Over 1000 Designer Frames <em>&amp; Sunglasses</em></h3>
  <div class="abs rule" style="top:795px;left:186px;width:75px"></div>
  <div class="abs label-row" style="top:816px"><span>Aurelio</span><span>Lena Park</span><span>Verano</span><span>Cristalle</span><span>Linea</span><span>Maison Belle</span></div>
  <div class="abs label-row" style="top:840px"><span>Thorne</span><span>Valente</span><span>Marina</span><span>Summit</span><span>Solaro</span><span>Kaia</span></div>
  <span class="abs more">&amp; MORE</span>

  <svg class="abs contact-band" viewBox="0 0 447 137" preserveAspectRatio="none"><path d="M0 14 Q220 -6 447 12 V137 H0Z" fill="var(--sky)"/></svg>
  <div class="abs contact" style="left:23px;top:902px"><span class="contact__icon"><svg width="12" height="12" viewBox="0 0 12 12"><path d="M6 0 A4 4 0 0 1 10 4 C10 7 6 12 6 12 C6 12 2 7 2 4 A4 4 0 0 1 6 0Z" fill="var(--navy)"/><circle cx="6" cy="4" r="1.5" fill="#fff"/></svg></span>418 Oakridge Pkwy,<br>Maple Hollow TX 75012</div>
  <div class="abs contact" style="left:226px;top:902px"><span class="contact__icon"><svg width="12" height="12" viewBox="0 0 12 12"><path d="M2 0 L4.5 0 L5.5 3 L4 4.2 Q5 7 7.8 8 L9 6.5 L12 7.5 V10 Q12 12 10 12 Q0 11 0 2 Q0 0 2 0Z" fill="var(--navy)"/></svg></span>Call or Text for Appointment<br>555.014.2290</div>
  <div class="abs contact" style="left:23px;top:947px"><span class="contact__icon"><svg width="12" height="12" viewBox="0 0 12 12"><circle cx="6" cy="6" r="6" fill="var(--navy)"/><path d="M6 2.5V6H8.5" fill="none" stroke="#fff" stroke-width="1.3"/></svg></span>M, T, Th, F 8:30-6.<br>W-10-6</div>
  <div class="abs contact" style="left:226px;top:947px"><span class="contact__icon"><svg width="12" height="12" viewBox="0 0 12 12"><circle cx="6" cy="6" r="5.3" fill="none" stroke="var(--navy)" stroke-width="1.2"/><ellipse cx="6" cy="6" rx="2.3" ry="5.3" fill="none" stroke="var(--navy)" stroke-width="1"/><path d="M0.7 6H11.3" stroke="var(--navy)" stroke-width="1"/></svg></span>www.ClearviewEyeStudio.com</div>
</section>
</body>
</html>
```